professional business card design

Business card design. Photos have been uploaded and i am open to the designer choosing which photos to use. Would like the card to be mostyly in a grey scale design with black, whites, silver & grey colours. I have added copy of our flyer as would like on the back side of card our services to be listed. Do not use any bright colurs such as blue red green or yellow. i need to be able to edit the phone number and naem in the final card design submitted.

Target Market(s)

Clients

Industry/Entity Type

earhmovibng and transport

Contact Information for Business Card

Director Name, address, email, phone number and services

Colors

Designer to choose only greyscale colors for use in the design.

Requirements
Should not have
• no yellow, red, blue or green

```html
<!DOCTYPE html>
<html lang="en">
<head>
<meta charset="utf-8">
<title>KTR Pty Ltd – Business Card</title>
<link rel="stylesheet" href="https://fonts.googleapis.com/css2?family=Arimo:ital,wght@0,400;0,700;1,700&display=swap">
<style>
  :root {
    --board-top: #f7f7f7;
    --board-bottom: #d6d6d6;
    --label: #2a2a2a;
    --card-black: #000000;
    --card-mid: #3a3a3a;
    --card-glow: #5a5a5a;
    --white: #ffffff;
    --silver: #d9d9d9;
    --band-light: #bdbdbd;
    --band-mid: #7a7a7a;
    --row-text-dark: #111111;
    --photo-light: #9a9a9a;
    --photo-dark: #2b2b2b;
  }
  * { margin: 0; padding: 0; box-sizing: border-box; }
  html, body { width: 1200px; height: 1200px; overflow: hidden; }
  body {
    position: relative;
    background: linear-gradient(180deg, var(--board-top), var(--board-bottom));
    font-family: "Arimo", Arial, sans-serif;
  }
  .side-label {
    position: absolute;
    left: 212px;
    font-size: 56px;
    font-weight: 400;
    color: var(--label);
    line-height: 1;
  }
  .side-label--front { top: 46px; }
  .side-label--back { top: 602px; left: 217px; }

  .card {
    position: absolute;
    left: 213px;
    width: 774px;
    height: 442px;
    overflow: hidden;
    border: 1px solid #555;
    background:
      radial-gradient(ellipse 55% 60% at 50% 30%, var(--card-glow) 0%, var(--card-mid) 35%, var(--card-black) 80%);
    color: var(--white);
  }
  .card--front { top: 115px; }
  .card--back {
    top: 670px;
    background:
      radial-gradient(ellipse 55% 45% at 50% 15%, var(--card-glow) 0%, var(--card-mid) 40%, var(--card-black) 85%);
  }

  /* Front */
  .holder-name {
    position: absolute; left: 40px; top: 34px;
    font-size: 50px; font-weight: 700; line-height: 1;
  }
  .holder-role {
    position: absolute; left: 41px; top: 88px;
    font-size: 34px; font-weight: 400; line-height: 1;
  }
  .brand {
    position: absolute; left: 415px; top: 38px;
    display: flex; align-items: flex-end; gap: 10px;
  }
  .brand-name {
    font-size: 84px; font-weight: 700; line-height: 1;
    color: var(--silver); letter-spacing: 4px;
  }
  .brand-suffix {
    font-size: 16px; font-weight: 700; color: var(--silver);
    margin-bottom: 10px;
  }
  .contact-list {
    position: absolute; left: 46px; top: 148px;
    list-style: none;
  }
  .contact-item {
    display: flex; align-items: flex-start; gap: 14px;
    font-size: 20px; line-height: 22px; margin-bottom: 11px;
  }
  .contact-icon { width: 24px; height: 24px; flex: none; }
  .hero-photo {
    position: absolute; left: 62px; top: 278px; width: 657px; height: 164px;
    background: linear-gradient(180deg, rgba(80,80,80,0) 0%, var(--photo-light) 35%, var(--photo-dark) 100%);
  }

  /* Back */
  .back-brand {
    position: absolute; left: 92px; top: 40px;
    font-size: 92px; font-weight: 700; line-height: 1;
    color: var(--silver); letter-spacing: 4px;
  }
  .services-title {
    position: absolute; left: 364px; top: 80px;
    font-size: 41px; font-weight: 700; font-style: italic;
    color: var(--silver); line-height: 1;
  }
  .service-list {
    position: absolute; list-style: none;
  }
  .service-list--left { left: 114px; top: 134px; width: 274px; }
  .service-list--right { left: 393px; top: 133px; width: 248px; }
  .service {
    display: flex; align-items: center; gap: 8px;
    height: 23.8px; padding-left: 6px;
    font-size: 14.5px; font-weight: 700; color: var(--white);
  }
  .service--banded {
    background: linear-gradient(90deg, var(--band-light) 0%, var(--band-mid) 55%, rgba(0,0,0,0) 100%);
    color: var(--row-text-dark);
  }
  .service--tall { height: 37px; align-items: flex-start; padding-top: 2px; line-height: 17px; }
  .tick { width: 12px; height: 12px; flex: none; }
  .service--tall .tick { margin-top: 3px; }
  .fleet-photo {
    position: absolute; left: 66px; top: 272px; width: 629px; height: 147px;
    background: linear-gradient(180deg, rgba(80,80,80,0) 0%, var(--photo-light) 40%, var(--photo-dark) 100%);
  }
</style>
</head>
<body>
  <div class="side-label side-label--front">Front</div>

  <section class="card card--front">
    <div class="hero-photo" role="img" aria-label="Black and white photo of a road train truck with three tipper trailers on an outback road"></div>
    <h1 class="holder-name">Your Name</h1>
    <div class="holder-role">DIRECTOR</div>
    <div class="brand">
      <span class="brand-name">KTR</span>
      <span class="brand-suffix">Pty Ltd</span>
    </div>
    <ul class="contact-list">
      <li class="contact-item">
        <svg class="contact-icon" viewBox="0 0 24 24"><circle cx="12" cy="12" r="12" fill="#fff"/><circle cx="12" cy="12" r="6" fill="none" stroke="#000" stroke-width="2.5"/><circle cx="12" cy="12" r="2" fill="#000"/></svg>
        <span>Depot: Lot 114,<br>Ridgeback Road Marlow Creek</span>
      </li>
      <li class="contact-item">
        <svg class="contact-icon" viewBox="0 0 24 24"><circle cx="12" cy="12" r="12" fill="#fff"/><path d="M5 10 L19 7 L13 18 L11.5 13 Z" fill="#000"/></svg>
        <span>email</span>
      </li>
      <li class="contact-item">
        <svg class="contact-icon" viewBox="0 0 24 24"><circle cx="12" cy="12" r="12" fill="#fff"/><path d="M8 6 L10.5 6 L11.5 9 L10 10.5 Q11.5 13.5 13.5 14.5 L15 13 L18 14 L18 16.5 Q17 18 15 18 Q7 16 6 8 Q6 6.5 8 6 Z" fill="#000"/></svg>
        <span>phone number</span>
      </li>
    </ul>
  </section>

  <div class="side-label side-label--back">Back</div>

  <section class="card card--back">
    <div class="back-brand">KTR</div>
    <h2 class="services-title">OUR SERVICES</h2>

    <ul class="service-list service-list--left">
      <li class="service service--banded"><svg class="tick" viewBox="0 0 12 12"><circle cx="6" cy="6" r="5.2" fill="none" stroke="currentColor" stroke-width="1"/><path d="M3.5 6 L5.3 7.8 L8.6 4.4" fill="none" stroke="currentColor" stroke-width="1.2"/></svg>Over size loads / Hot Shot Loads</li>
      <li class="service"><svg class="tick" viewBox="0 0 12 12"><circle cx="6" cy="6" r="5.2" fill="none" stroke="currentColor" stroke-width="1"/><path d="M3.5 6 L5.3 7.8 L8.6 4.4" fill="none" stroke="currentColor" stroke-width="1.2"/></svg>Heavy Vehicle Recovery Services</li>
      <li class="service service--banded"><svg class="tick" viewBox="0 0 12 12"><circle cx="6" cy="6" r="5.2" fill="none" stroke="currentColor" stroke-width="1"/><path d="M3.5 6 L5.3 7.8 L8.6 4.4" fill="none" stroke="currentColor" stroke-width="1.2"/></svg>Potable Water Deliveries</li>
      <li class="service"><svg class="tick" viewBox="0 0 12 12"><circle cx="6" cy="6" r="5.2" fill="none" stroke="currentColor" stroke-width="1"/><path d="M3.5 6 L5.3 7.8 L8.6 4.4" fill="none" stroke="currentColor" stroke-width="1.2"/></svg>Road Building / Maintenance</li>
      <li class="service service--banded"><svg class="tick" viewBox="0 0 12 12"><circle cx="6" cy="6" r="5.2" fill="none" stroke="currentColor" stroke-width="1"/><path d="M3.5 6 L5.3 7.8 L8.6 4.4" fill="none" stroke="currentColor" stroke-width="1.2"/></svg>Earthworks</li>
      <li class="service"><svg class="tick" viewBox="0 0 12 12"><circle cx="6" cy="6" r="5.2" fill="none" stroke="currentColor" stroke-width="1"/><path d="M3.5 6 L5.3 7.8 L8.6 4.4" fill="none" stroke="currentColor" stroke-width="1.2"/></svg>sand &amp; Metal Supply &amp; Cartage</li>
    </ul>

    <ul class="service-list service-list--right">
      <li class="service service--banded"><svg class="tick" viewBox="0 0 12 12"><circle cx="6" cy="6" r="5.2" fill="none" stroke="currentColor" stroke-width="1"/><path d="M3.5 6 L5.3 7.8 L8.6 4.4" fill="none" stroke="currentColor" stroke-width="1.2"/></svg>Road Train Tippers</li>
      <li class="service"><svg class="tick" viewBox="0 0 12 12"><circle cx="6" cy="6" r="5.2" fill="none" stroke="currentColor" stroke-width="1"/><path d="M3.5 6 L5.3 7.8 L8.6 4.4" fill="none" stroke="currentColor" stroke-width="1.2"/></svg>Road Train Tankers</li>
      <li class="service service--banded"><svg class="tick" viewBox="0 0 12 12"><circle cx="6" cy="6" r="5.2" fill="none" stroke="currentColor" stroke-width="1"/><path d="M3.5 6 L5.3 7.8 L8.6 4.4" fill="none" stroke="currentColor" stroke-width="1.2"/></svg>Road Train Flat Tops</li>
      <li class="service"><svg class="tick" viewBox="0 0 12 12"><circle cx="6" cy="6" r="5.2" fill="none" stroke="currentColor" stroke-width="1"/><path d="M3.5 6 L5.3 7.8 L8.6 4.4" fill="none" stroke="currentColor" stroke-width="1.2"/></svg>Drop Deck Trailers</li>
      <li class="service service--banded service--tall"><svg class="tick" viewBox="0 0 12 12"><circle cx="6" cy="6" r="5.2" fill="none" stroke="currentColor" stroke-width="1"/><path d="M3.5 6 L5.3 7.8 L8.6 4.4" fill="none" stroke="currentColor" stroke-width="1.2"/></svg><span>Mine Site accredited<br>equipment &amp; Operators</span></li>
    </ul>

    <div class="fleet-photo" role="img" aria-label="Black and white montage of the fleet: tankers, oversize load truck, machinery carrier and prime movers"></div>
  </section>
</body>
</html>
```